vantoreq realty business card

We need a Business card for our new business. The logo was designed by BrushQuill, and the text We want on the back is:
REAL ESTATE INVESTMENTS
- BUY, RENOVATE, SELL AND RENT RESIDENTIAL PROPERTIES
- FULL HOME REHABBING , REMODELING AND INTERIOR DESIGN
- HOME STAGING SERVICES
- WHOLESALE INVESTOR PROPERTIES
- MAKE CASH OFFERS ON HOUSES IN ANY CONDITION AND IN ANY SITUATION
- PRIVATE MONEY INVESTOR PROGRAMS WITH 6-12% RETURNS
- PAY CASH REWARDS FOR REFFERALS
- CONCIERGE SERVICE

Business

```html
<!DOCTYPE html>
<html lang="en">
<head>
<meta charset="utf-8">
<title>Vantoreq Realty – Business Card</title>
<link href="https://fonts.googleapis.com/css2?family=Open+Sans:wght@400;600&display=swap" rel="stylesheet">
<style>
  :root {
    --canvas-bg: #e9e9e7;
    --teal: #73c7cc;
    --teal-ink: #3d7d84;
    --teal-accent: #5cc0c9;
    --white: #ffffff;
    --grey-ink: #6b6c6f;
    --grey-soft: #9a9b9e;
  }
  * { margin: 0; padding: 0; box-sizing: border-box; }
  html, body {
    width: 1200px; height: 1000px; overflow: hidden;
    background: var(--canvas-bg);
    font-family: "Open Sans", Arial, sans-serif;
  }
  .canvas {
    width: 1200px; height: 1000px;
    display: flex; flex-direction: column; align-items: center; justify-content: center;
    gap: 40px;
  }
  .card {
    width: 760px; height: 434px;
    position: relative;
    box-shadow: 0 2px 6px rgba(0,0,0,0.18);
  }
  /* Front */
  .card--front {
    background: var(--teal);
    display: flex; flex-direction: column; align-items: center;
  }
  .card--front .brand { margin-top: 150px; text-align: center; }
  .brand__name {
    font-size: 30px; font-weight: 400; letter-spacing: 0.5px; line-height: 1;
  }
  .brand__tagline {
    font-size: 13px; letter-spacing: 1.6px; margin-top: 8px;
  }
  .card--front .brand__name { color: var(--white); }
  .card--front .brand__tagline { color: #d8f0f1; }
  .contact-line {
    position: absolute; bottom: 70px; left: 0; right: 0;
    text-align: center;
    color: var(--teal-ink);
    font-size: 17px; letter-spacing: 0.3px;
  }
  /* Back */
  .card--back {
    background: var(--white);
    display: flex; flex-direction: column; align-items: center;
  }
  .card--back .brand { margin-top: 56px; text-align: center; }
  .card--back .brand__name { color: var(--teal-accent); font-size: 28px; }
  .card--back .brand__tagline { color: var(--grey-soft); }
  .services {
    list-style: none;
    margin-top: 60px;
    text-align: center;
    color: var(--grey-ink);
    font-size: 14.5px; line-height: 23px; letter-spacing: 0.2px;
  }
  .services li { display: flex; align-items: center; justify-content: center; gap: 8px; }
  .services svg { width: 10px; height: 10px; flex: none; }
</style>
</head>
<body>
<main class="canvas">
  <section class="card card--front" aria-label="Business card front">
    <div class="brand">
      <div class="brand__name">VANTOREQ Realty</div>
      <div class="brand__tagline">REAL ESTATE SOLUTIONS</div>
    </div>
    <p class="contact-line">John Doe | 000 000 0000 | email@mailpost.com | www.website.com</p>
  </section>

  <section class="card card--back" aria-label="Business card back">
    <div class="brand">
      <div class="brand__name">VANTOREQ Realty</div>
      <div class="brand__tagline">REAL ESTATE SOLUTIONS</div>
    </div>
    <svg width="0" height="0" style="position:absolute">
      <defs>
        <symbol id="bullet" viewBox="0 0 10 10">
          <circle cx="5" cy="5" r="5" fill="#5cc0c9"/>
          <path d="M4 2.8 L6.2 5 L4 7.2" fill="none" stroke="#fff" stroke-width="1.4"/>
        </symbol>
      </defs>
    </svg>
    <ul class="services">
      <li><svg><use href="#bullet"/></svg>BUY, RENOVATE, SELL AND RENT RESIDENTIAL PROPERTIES</li>
      <li><svg><use href="#bullet"/></svg>FULL HOME REHABBING , REMODELING AND INTERIOR DESIGN</li>
      <li><svg><use href="#bullet"/></svg>HOME STAGING SERVICES</li>
      <li><svg><use href="#bullet"/></svg>WHOLESALE INVESTOR PROPERTIES</li>
      <li><svg><use href="#bullet"/></svg>MAKE CASH OFFERS ON HOUSES IN ANY CONDITION AND IN ANY SITUATION</li>
      <li><svg><use href="#bullet"/></svg>PRIVATE MONEY INVESTOR PROGRAMS WITH 6-12% RETURNS</li>
      <li><svg><use href="#bullet"/></svg>PAY CASH REWARDS FOR REFFERALS</li>
      <li><svg><use href="#bullet"/></svg>CONCIERGE SERVICE</li>
    </ul>
  </section>
</main>
</body>
</html>
```